modern design for software startup

We need a website design. We are a software company developing a cruise management system for cruise ships. We don't want or need something elaborate. In fact, we don't want to show specifics of our products because they are under development and we do not want our competitors to know too much. We want to focus on ideals and principals of our company and hint at what we are doing.

Target Market(s)

cruise lines

Industry/Entity Type

Software

Coding

Coded - Design and coding required

Number of Pages Required

1 page

Font styles to use
Sans Serif

Colors
7f7f7f
5c5c5c

Requirements
Must have
• background pictures of cruise ships, ports, ocean, some developers working on computers in brown and white and fuzzy. can't show specific cruise lines. magazine like style. white text. links at bottom to facebook, twitter, instagram
• email link for investor/partner inquiries.
Nice to have
• Some inspirational quotes here and there. Not overpowering but subtle. content to be provided in text file.
• color schemes - we like the scheme in www.tindelmarsh.com
• doesnt have to be exact but similar is good.

```html
<!DOCTYPE html>
<html lang="en">
<head>
<meta charset="utf-8">
<title>Halvane Software</title>
<link href="https://fonts.googleapis.com/css2?family=Poppins:wght@500;600&family=Open+Sans:wght@400;600&display=swap" rel="stylesheet">
<style>
:root{
  --ink:#111418;
  --navy:#1b2a44;
  --grey-dark:#5c5c5c;
  --grey:#7f7f7f;
  --panel:#4f4f4f;
  --accent:#3aa6dc;
  --rule:#9ab6cc;
  --footer:#1d1d1d;
  --footer-field:#2b2b2b;
  --white:#ffffff;
  --body-text:#4a4a4a;
}
*{margin:0;padding:0;box-sizing:border-box}
html,body{width:1200px;height:3226px;overflow:hidden;background:var(--white)}
body{position:relative;font-family:"Open Sans",Arial,sans-serif;color:var(--body-text)}
.abs{position:absolute}
.heading{font-family:"Poppins",Arial,sans-serif;font-weight:600;text-transform:uppercase;color:var(--ink)}

/* header */
.site-header{left:0;top:0;width:1200px;height:122px;background:linear-gradient(#fdfdfd,#f2f4f6)}
.brand{left:60px;top:48px;display:flex;align-items:center;gap:10px;font-family:"Poppins",Arial,sans-serif;font-weight:600;font-size:27px;color:var(--navy);letter-spacing:1px}
.brand-dot{width:16px;height:16px;border-radius:50%;background:var(--navy)}
.phone-box{left:940px;top:15px;width:200px;height:42px;background:var(--grey-dark);color:var(--white);display:flex;align-items:center;gap:16px;padding-left:14px;font-family:"Poppins",Arial,sans-serif;font-weight:500;font-size:21px;letter-spacing:1px}
.nav{left:447px;top:68px;display:flex;gap:0;font-family:"Poppins",Arial,sans-serif;font-weight:600;font-size:14.5px;color:var(--ink)}
.nav a{display:block;padding:8px 18px;color:inherit;text-decoration:none;margin-right:10px}
.nav a.active{background:var(--grey-dark);color:var(--white)}

/* hero */
.hero{left:0;top:122px;width:1200px;height:636px;background:linear-gradient(180deg,#8fb1d2 0%,#c9d8e6 38%,#5d7fa3 62%,#24446b 100%)}
.hero-card{left:60px;top:335px;width:590px;height:182px;background:rgba(235,240,245,.78);padding:20px 18px}
.hero-title{font-size:38px;line-height:44px;color:var(--navy)}
.hero-btn{margin-top:26px;display:inline-block;background:var(--grey-dark);color:var(--white);font-size:17px;font-weight:600;padding:7px 18px}

/* about */
.section-title{width:1200px;left:0;text-align:center}
.divider{height:2px;background:var(--rule)}
.divider-mark{width:10px;height:10px;background:var(--accent);transform:rotate(45deg)}
.about-copy{left:140px;top:915px;width:920px;text-align:center;font-size:15.5px;line-height:28px;color:var(--grey-dark)}
.btn{background:var(--grey-dark);color:var(--white);font-weight:600;font-size:17px;display:flex;align-items:center;justify-content:center;border:2px solid #9a9a9a}

/* commitment */
.commit-photo{left:0;top:1140px;width:760px;height:450px;background:linear-gradient(120deg,#cfd8de 0%,#9aa8b2 45%,#7a7670 100%)}
.commit-panel{left:620px;top:1140px;width:580px;height:450px;background:linear-gradient(90deg,rgba(79,79,79,0) 0%,var(--panel) 14%,var(--panel) 100%)}
.commit-title{left:648px;top:1205px;width:520px;font-size:33px;line-height:40px;color:var(--white)}
.commit-copy{left:650px;top:1308px;width:500px;font-size:14.5px;line-height:26px;color:var(--white)}

/* care think do */
.ctd-title{display:flex;justify-content:center;align-items:center;gap:14px;font-size:40px}
.ctd-sep{width:9px;height:9px;background:var(--accent);transform:rotate(45deg)}
.ctd-copy{left:140px;top:1778px;width:920px;text-align:center;font-size:15.5px;line-height:27px;color:var(--body-text)}

/* testimonials */
.testimonials{left:0;top:2032px;width:1200px;height:476px;background:linear-gradient(180deg,#4e5256 0%,#5e6266 50%,#505356 100%)}
.avatar{left:548px;top:2190px;width:104px;height:104px;border-radius:50%;background:linear-gradient(160deg,#e9e4dc,#b7a28c);border:4px solid var(--white)}
.arrow-btn{width:42px;height:38px;background:var(--white);display:flex;align-items:center;justify-content:center}
.quote-mark{left:148px;top:2296px;font-family:"Poppins",Arial,sans-serif;font-size:90px;line-height:80px;color:var(--accent);font-weight:600}
.quote-copy{left:190px;top:2324px;width:860px;text-align:center;font-size:15.5px;line-height:26px;color:var(--white)}
.quote-name{left:0;top:2414px;width:1200px;text-align:center;font-family:"Poppins",Arial,sans-serif;font-weight:600;font-size:21px;color:var(--accent)}

/* signup */
.signup-sub{left:0;top:2634px;width:1200px;text-align:center;font-size:15px;color:var(--grey-dark)}
.signup-input{left:322px;top:2690px;width:486px;height:36px;border:1px solid #cfcfcf;font-size:14px;color:#9a9a9a;padding:8px 10px}
.signup-btn{left:808px;top:2690px;width:108px;height:36px;background:var(--grey-dark);color:var(--white);font-weight:600;font-size:14px;display:flex;align-items:center;justify-content:center}

/* footer */
.footer{left:0;top:2797px;width:1200px;height:429px;background:var(--footer)}
.foot-head{font-family:"Poppins",Arial,sans-serif;font-weight:500;font-size:16px;color:var(--white);text-transform:uppercase}
.foot-rule{width:30px;height:2px;background:var(--white);margin-top:10px}
.foot-line{display:flex;align-items:flex-start;gap:14px;font-size:13.5px;line-height:22px;color:#d6d6d6}
.social{display:flex;gap:12px}
.social span{width:28px;height:28px;border:1px solid #6a6a6a;border-radius:50%}
.news-item{font-size:13.5px;color:#e2e2e2}
.news-date{font-size:10.5px;color:#8d8d8d;margin-top:4px}
.foot-about{font-size:13px;line-height:26px;color:#cfcfcf}
.field{background:var(--footer-field);color:#cfcfcf;font-size:12px;padding:8px 12px;text-transform:uppercase}
.send{background:var(--accent);color:var(--white);font-size:15px;display:flex;align-items:center;justify-content:center}
.copyright{left:0;top:3198px;width:1200px;text-align:center;font-size:13px;color:#bdbdbd}
</style>
</head>
<body>

<header class="abs site-header">
  <div class="abs brand"><span class="brand-dot"></span>HALVANE SOFTWARE</div>
  <div class="abs phone-box">
    <svg width="20" height="20" viewBox="0 0 24 24"><path fill="#fff" d="M6.6 10.8a15 15 0 0 0 6.6 6.6l2.2-2.2a1 1 0 0 1 1-.25 11.4 11.4 0 0 0 3.6.6 1 1 0 0 1 1 1V20a1 1 0 0 1-1 1A17 17 0 0 1 3 4a1 1 0 0 1 1-1h3.5a1 1 0 0 1 1 1c0 1.25.2 2.45.6 3.6a1 1 0 0 1-.25 1z"/></svg>
    555010228
  </div>
  <nav class="abs nav">
    <a class="active" href="#">HOME</a><a href="#">OUR STORY</a><a href="#">PRODUCTS</a><a href="#">WHY SUPREME</a><a href="#">NEWS</a><a href="#">CONTACT US</a>
  </nav>
</header>

<section class="abs hero" role="img" aria-label="Cruise ship sailing on open ocean under a cloudy blue sky"></section>
<div class="abs hero-card">
  <h1 class="heading hero-title">Blue swimming crab from<br>ocean to table</h1>
  <span class="hero-btn">Find Your Service</span>
</div>

<h2 class="abs heading section-title" style="top:822px;font-size:34px">About Halvane Software</h2>
<div class="abs divider" style="left:303px;top:884px;width:607px"></div>
<div class="abs divider-mark" style="left:590px;top:879px"></div>
<p class="abs about-copy">We empower our Halvane family to speak their mind and share their ideas, no matter how outside the box or crazy they are.<br>We champion our team to challenge the status Quo and to set new standards to change the way business is done and<br>to instill Optimism in everyone.</p>
<div class="abs btn" style="left:484px;top:1035px;width:139px;height:44px">Learn more</div>
<div class="abs btn" style="left:630px;top:1035px;width:139px;height:44px">Contact us</div>

<section class="abs commit-photo" role="img" aria-label="Software team working at computers in a bright office"></section>
<div class="abs commit-panel"></div>
<h2 class="abs heading commit-title">Halvane's commitment to our planet</h2>
<p class="abs commit-copy">Technology is one of the largest contributor of pollution on our planet. According to the US EPA, more than 4.6 million tonnes of e-waste ended up in US landfills in 2000. Toxic chemicals in electronics products can leach into the land over time or are released into the atmosphere, impacting nearby communities and the environment. Our technology's benefit is that it works not only on the latest devices, it works on legacy systems allowing our clients to maintain older functioning technology longer keeping it our of land fills longer.</p>

<h2 class="abs heading section-title ctd-title" style="top:1668px">Care<span class="ctd-sep"></span>Think<span class="ctd-sep"></span>Do</h2>
<div class="abs divider" style="left:332px;top:1730px;width:545px"></div>
<div class="abs ctd-copy">
  <p>Courageously leading our customers, partners, and ourselves to success by caring, thinking, and doing. Courageously leading our customers, partners, and ourselves to success by caring, thinking, and doing. Courageously leading our customers, partners, and ourselves to success by caring, thinking, and doing. Courageously leading our customers, partners, and ourselves<br>to success by caring, thinking, and doing.</p>
  <p style="margin-top:18px">Courageously leading our customers, partners, and ourselves to success by caring, thinking, and doing.</p>
</div>

<section class="abs testimonials" role="img" aria-label="Faded cruise ship on the sea behind the testimonials"></section>
<h2 class="abs heading section-title" style="top:2094px;font-size:38px;color:var(--white)">Testimonials</h2>
<div class="abs arrow-btn" style="left:476px;top:2228px"><svg width="20" height="14" viewBox="0 0 20 14"><path d="M19 7H2M7 1 1 7l6 6" stroke="#111" stroke-width="2" fill="none"/></svg></div>
<div class="abs avatar" role="img" aria-label="Portrait of the client giving the testimonial"></div>
<div class="abs arrow-btn" style="left:692px;top:2228px"><svg width="20" height="14" viewBox="0 0 20 14"><path d="M1 7h17M13 1l6 6-6 6" stroke="#111" stroke-width="2" fill="none"/></svg></div>
<div class="abs quote-mark">&ldquo;</div>
<p class="abs quote-copy">We are pleased to say that work done by this company is outstanding. Everything what we asked was done on time and with high precision by the professional team. With proper briefing there is no room for any mistakes. During the project execution team has applied requested changes in professional manner.</p>
<div class="abs quote-name">-Maren Holt</div>

<h2 class="abs heading section-title" style="top:2584px;font-size:38px">Signup below to get news</h2>
<div class="abs signup-sub">Subscribe to our mailing list</div>
<div class="abs signup-input">Your Email</div>
<div class="abs signup-btn">Subscribe</div>

<footer class="abs footer"></footer>
<div class="abs" style="left:70px;top:2846px">
  <div class="foot-head">Contacts</div><div class="foot-rule"></div>
  <div class="foot-line" style="margin-top:26px"><svg width="14" height="14" viewBox="0 0 24 24"><path fill="#ddd" d="M6.6 10.8a15 15 0 0 0 6.6 6.6l2.2-2.2a1 1 0 0 1 1-.25 11.4 11.4 0 0 0 3.6.6 1 1 0 0 1 1 1V20a1 1 0 0 1-1 1A17 17 0 0 1 3 4a1 1 0 0 1 1-1h3.5a1 1 0 0 1 1 1c0 1.25.2 2.45.6 3.6a1 1 0 0 1-.25 1z"/></svg>(800) 555 01 47</div>
  <div class="foot-line" style="margin-top:20px"><svg width="14" height="14" viewBox="0 0 24 24"><rect x="2" y="5" width="20" height="14" fill="none" stroke="#ddd" stroke-width="2"/><path d="M2 6l10 7 10-7" fill="none" stroke="#ddd" stroke-width="2"/></svg>hello@halvane.example</div>
  <div class="foot-line" style="margin-top:20px"><svg width="14" height="14" viewBox="0 0 24 24"><path fill="#ddd" d="M12 2a7 7 0 0 0-7 7c0 5 7 13 7 13s7-8 7-13a7 7 0 0 0-7-7zm0 9.5A2.5 2.5 0 1 1 12 6.5a2.5 2.5 0 0 1 0 5z"/></svg>48 Harbour Lane, Portsea, Coastal<br>4100, Australia</div>
  <div class="social" style="margin-top:24px"><span></span><span></span><span></span><span></span><span></span><span></span></div>
</div>
<div class="abs" style="left:344px;top:2846px">
  <div class="foot-head">Latest News</div><div class="foot-rule"></div>
  <div class="news-item" style="margin-top:26px">This is a Audio post Type</div><div class="news-date">January 5, 2016</div>
  <div class="news-item" style="margin-top:14px">This is a Gallery post Type</div><div class="news-date">January 5, 2016</div>
  <div class="news-item" style="margin-top:14px">This is a Quote post Type</div><div class="news-date">January 5, 2016</div>
  <div class="news-item" style="margin-top:14px">Post Video</div><div class="news-date">October 2, 2015</div>
</div>
<div class="abs" style="left:585px;top:2846px;width:240px">
  <div class="foot-head">About</div><div class="foot-rule"></div>
  <p class="foot-about" style="margin-top:24px">Cum sociis natoque penatibus et magnis dis parturient montes, nascetur ridiculus mus. Etiam imperdiet. Ut sollicitudin sem sit amet ipsum. In id dui. Pellentesque sapien. Curabitur commodo elit eget erat. Aliquam sit amet nibh. Ut vitae elit. Donec ac nisi eget.</p>
</div>
<div class="abs" style="left:884px;top:2846px;width:234px">
  <div class="foot-head">Quick Contact</div><div class="foot-rule"></div>
  <div class="field" style="margin-top:26px;height:36px">Your Name</div>
  <div class="field" style="margin-top:8px;height:36px">Your Email</div>
  <div class="field" style="margin-top:8px;height:92px">Message...</div>
  <div class="send" style="margin-top:14px;width:76px;height:34px">Send</div>
</div>
<div class="abs" style="left:60px;top:3180px;width:1080px;height:1px;background:#333"></div>
<div class="abs copyright">&copy; 2016 Halvane Software Right Reserved.</div>

</body>
</html>
```